We are looking for Facebook and Instagram templates. To use both platforms we will use square images. We need a template for our posts, not the header image.
Most posts contain multiple images and we need a designoverlay in which we can embed our images.
Attached a screenshot of our website www.velaroo.be, our logo in svg and ai. The monkey is our mascotte (excact this monkey, not another).
We offer teambuildings, the style should be fun. Colors are antracite, limegreen and white. I did attache the current layout for posts but we are not happy with this.
If we could have some small design elements (like stickers) we can always create a new layout but is feels the same.
Our website is quite simple, this should also be in these post designs. Simple forms, rounded corners.

Allow more time for the designers, good work requires more time

Teambuilding

Teambuilding

• RobotoSlab

• If we could have some small design elements (like stickers) we can always create a new layout but is feels the same.
• Complex design, simple images works best for us

```html
<!DOCTYPE html>
<html lang="nl">
<head>
<meta charset="utf-8">
<title>Velaroo social post templates</title>
<link rel="stylesheet" href="https://fonts.googleapis.com/css2?family=Poppins:wght@400;500;700;800&family=Bebas+Neue&family=Oswald:wght@600&display=swap">
<style>
  :root {
    --stage: #a7a7a7;
    --anthracite: #2b2b2b;
    --anthracite-deep: #1d1d1d;
    --lime: #a6d116;
    --lime-bright: #b9e21c;
    --foliage: rgba(166, 209, 22, 0.28);
    --foliage-strong: rgba(166, 209, 22, 0.55);
    --white: #ffffff;
    --photo-forest: #6f8456;
    --photo-house: #9a8f78;
    --drum-tone: #c9b13a;
  }
  * { margin: 0; padding: 0; box-sizing: border-box; }
  html, body { width: 1200px; height: 696px; overflow: hidden; }
  body { background: var(--stage); position: relative; font-family: "Poppins", sans-serif; }

  .post {
    position: absolute; top: 92px; width: 486px; height: 486px; overflow: hidden;
    background: radial-gradient(circle at 70% 40%, #3a3a3a 0%, var(--anthracite) 45%, var(--anthracite-deep) 100%);
  }
  .post--bouwverlof { left: 85px; }
  .post--ontdekking { left: 627px; }

  .brand {
    position: absolute; left: 36px; top: 48px;
    font: 800 28px/1 "Poppins", sans-serif; letter-spacing: 2px; color: var(--white);
    display: flex; align-items: center; gap: 8px;
  }
  .brand-dot { width: 12px; height: 12px; background: var(--lime); border-radius: 50%; }
  .post--ontdekking .brand { top: 54px; font-size: 26px; }

  .decor { position: absolute; border-radius: 10px; }
  .decor--foliage { background: var(--foliage); }
  .decor--mascot { background: var(--lime); }
  .decor--drum { background: linear-gradient(180deg, var(--foliage-strong), var(--drum-tone)); }

  .headline-inzet { position: absolute; left: 36px; top: 110px; font: 700 40px/1 "Poppins", sans-serif; color: var(--white); letter-spacing: 3px; }
  .headline-bouwverlof { position: absolute; left: 36px; top: 146px; font: 700 40px/1 "Poppins", sans-serif; color: var(--lime); letter-spacing: 1.5px; }
  .subline { position: absolute; left: 37px; top: 188px; font: 500 14px/17px "Poppins", sans-serif; color: var(--white); }
  .subline strong { color: var(--lime); font-weight: 700; display: block; }

  .photo {
    position: absolute; border: 5px solid var(--white); border-radius: 4px;
    box-shadow: 0 4px 10px rgba(0,0,0,.45);
  }
  .photo--forest { background: linear-gradient(160deg, #8aa06a, var(--photo-forest) 60%, #b8a98a); }
  .photo--house { background: linear-gradient(170deg, #c7d6e4 0%, var(--photo-house) 45%, #5d6b45 100%); }
  .photo--group { background: linear-gradient(170deg, #6d9a4e, #c8c2b5 60%, #7fa05a); }

  .phone-pill {
    position: absolute; left: 85px; top: 442px; width: 129px; height: 19px;
    background: var(--lime); border-radius: 10px;
    display: flex; align-items: center; gap: 5px; padding-left: 3px;
    font: 500 14.5px/1 "Poppins", sans-serif; color: var(--anthracite-deep);
  }
  .phone-icon { width: 14px; height: 14px; background: var(--white); border-radius: 50%; display: flex; align-items: center; justify-content: center; }
  .website {
    position: absolute; left: 237px; top: 441px;
    font: 400 17px/1 "Poppins", sans-serif; letter-spacing: 2.6px; color: var(--white);
  }
  .website span { color: var(--lime); }

  .lime-band { position: absolute; left: 341px; top: 0; width: 117px; height: 486px; background: var(--lime-bright); }

  .headline-samen { position: absolute; left: 35px; top: 120px; font: 400 62px/1 "Bebas Neue", sans-serif; color: var(--white); }
  .headline-ontdekking { position: absolute; left: 35px; top: 169px; font: 400 64px/1 "Bebas Neue", sans-serif; color: var(--lime); }

  .offer-list { position: absolute; left: 35px; top: 242px; list-style: none; }
  .offer-list li {
    display: flex; align-items: center; gap: 9px; height: 32px;
    font: 600 14.5px/1 "Oswald", sans-serif; color: var(--white); letter-spacing: .3px;
  }
  .offer-icon { width: 24px; height: 20px; }
</style>
</head>
<body>

<section class="post post--bouwverlof">
  <div class="decor decor--foliage" role="img" aria-label="Jungle liaan met bladeren" style="left:220px;top:0;width:266px;height:80px;"></div>
  <div class="decor decor--foliage" role="img" aria-label="Jungle liaan met bladeren" style="left:380px;top:80px;width:106px;height:210px;"></div>
  <div class="decor decor--mascot" role="img" aria-label="Mascotte aapje op de liaan" style="left:345px;top:20px;width:58px;height:58px;"></div>
  <div class="decor decor--foliage" role="img" aria-label="Jungle bladeren" style="left:0;top:340px;width:70px;height:146px;"></div>

  <div class="brand">VELAROO <span class="brand-dot"></span></div>

  <h1 class="headline-inzet">INZET</h1>
  <h2 class="headline-bouwverlof">BOUWVERLOF</h2>
  <p class="subline">FULL HOUSE MET DE INZET VAN DE <strong>ZOMERVAKANTIE</strong></p>

  <div class="photo photo--house" role="img" aria-label="Foto van het groepsverblijf" style="left:36px;top:270px;width:178px;height:130px;transform:rotate(-8deg);"></div>
  <div class="photo photo--forest" role="img" aria-label="Foto van touwtrekken in het bos" style="left:197px;top:220px;width:172px;height:118px;transform:rotate(1deg);"></div>
  <div class="photo photo--group" role="img" aria-label="Groepsfoto met djembe" style="left:257px;top:312px;width:165px;height:116px;"></div>
  <div class="decor decor--drum" role="img" aria-label="Djembe trommel" style="left:412px;top:380px;width:74px;height:106px;"></div>

  <div class="phone-pill">
    <span class="phone-icon"><svg width="9" height="9" viewBox="0 0 24 24"><path d="M6.6 10.8a15 15 0 0 0 6.6 6.6l2.2-2.2c.3-.3.7-.4 1-.2 1.1.4 2.3.6 3.6.6.6 0 1 .4 1 1V20c0 .6-.4 1-1 1A17 17 0 0 1 3 4c0-.6.4-1 1-1h3.5c.6 0 1 .4 1 1 0 1.3.2 2.5.6 3.6.1.3 0 .7-.2 1z" fill="var(--anthracite-deep)"/></svg></span>
    0470918264
  </div>
  <p class="website">www.<span>velaroo</span>.be</p>
</section>

<section class="post post--ontdekking">
  <div class="lime-band"></div>
  <div class="decor decor--foliage" role="img" aria-label="Jungle liaan met bladeren" style="left:220px;top:0;width:266px;height:150px;"></div>
  <div class="decor decor--foliage" role="img" aria-label="Jungle bladeren" style="left:420px;top:400px;width:66px;height:86px;"></div>

  <div class="brand">VELAROO <span class="brand-dot"></span></div>

  <h1 class="headline-samen">SAMEN OP</h1>
  <h2 class="headline-ontdekking">ONTDEKKING</h2>

  <ul class="offer-list">
    <li><svg class="offer-icon" viewBox="0 0 24 20"><circle cx="12" cy="6" r="3.5" fill="var(--lime)"/><circle cx="5" cy="8" r="2.5" fill="var(--lime)"/><circle cx="19" cy="8" r="2.5" fill="var(--lime)"/><path d="M6 18a6 6 0 0 1 12 0z M0 18a5 5 0 0 1 8-4 M24 18a5 5 0 0 0-8-4" fill="var(--lime)"/></svg>TEAMBUILDING</li>
    <li><svg class="offer-icon" viewBox="0 0 24 20"><circle cx="9" cy="3" r="2.2" fill="var(--lime)"/><path d="M8 6l-3 6 3 1 1 6M9 8l4 3M8 13l-3 6" stroke="var(--lime)" stroke-width="2" fill="none"/><path d="M13 20L24 6v14z" fill="var(--lime)"/></svg>AVONTUUR</li>
    <li><svg class="offer-icon" viewBox="0 0 24 20"><path d="M14 3c1.5-2 5-1.5 5 1.5 0 2.5-5 6-5 6s-5-3.5-5-6C9 1.5 12.5 1 14 3z" fill="var(--lime)"/><path d="M1 14l5-2 6 2 5-1c1 0 1 1 0 2l-6 3-10-1z" fill="var(--lime)"/></svg>GELOVEN</li>
  </ul>

  <div class="photo photo--forest" role="img" aria-label="Foto van een groepsspel op het gras" style="left:284px;top:198px;width:124px;height:110px;transform:rotate(-8deg);"></div>
  <div class="photo photo--house" role="img" aria-label="Foto van het groepsverblijf" style="left:148px;top:294px;width:130px;height:130px;transform:rotate(-4deg);"></div>
  <div class="photo photo--forest" role="img" aria-label="Foto van touwtrekken in het bos" style="left:277px;top:310px;width:142px;height:104px;"></div>

  <div class="decor decor--mascot" role="img" aria-label="Mascotte aapje als silhouet" style="left:0;top:370px;width:80px;height:116px;"></div>

  <div class="phone-pill">
    <span class="phone-icon"><svg width="9" height="9" viewBox="0 0 24 24"><path d="M6.6 10.8a15 15 0 0 0 6.6 6.6l2.2-2.2c.3-.3.7-.4 1-.2 1.1.4 2.3.6 3.6.6.6 0 1 .4 1 1V20c0 .6-.4 1-1 1A17 17 0 0 1 3 4c0-.6.4-1 1-1h3.5c.6 0 1 .4 1 1 0 1.3.2 2.5.6 3.6.1.3 0 .7-.2 1z" fill="var(--anthracite-deep)"/></svg></span>
    0470918264
  </div>
  <p class="website">www.velaroo.be</p>
</section>

</body>
</html>
```